Korbin Ventilation's. "We're Dalton beyond the pack"!

Good day< Does your company do face mask? that is question 1. and lets finish the stationary design and I will pay for that now? 2 If your company has BLACK HATS now I would want to do some of those? 3 I notice do you do BANNER'S and or something I can put on van's magnet type or on a building! )k that's enough but for now lets start with the stationary stuff? let me know you should have my information, and the design look's GREAT!!! Thank you..

```html
<!DOCTYPE html>
<html lang="en">
<head>
<meta charset="utf-8">
<title>Korbin Ventilation's – Letterhead</title>
<link href="https://fonts.googleapis.com/css2?family=Lato:wght@300;400;700&family=Montserrat:wght@400;600&family=Pinyon+Script&display=swap" rel="stylesheet">
<style>
  :root{
    --bg:#e6e6e6;
    --paper:#f2f2f2;
    --ink:#3a3a3a;
    --ink-strong:#111;
    --green:#a3b243;
    --band:#3d3d3f;
    --white:#fff;
  }
  *{margin:0;padding:0;box-sizing:border-box}
  html,body{width:1200px;height:1200px;overflow:hidden;background:var(--bg)}
  .letterhead{
    position:absolute;left:203px;top:40px;width:793px;height:1120px;
    background:var(--paper);box-shadow:0 4px 18px rgba(0,0,0,.18);
    font-family:'Lato',sans-serif;font-weight:300;color:var(--ink);
  }
  .brand{position:absolute;left:40px;top:44px;width:206px;text-align:center;color:var(--ink-strong);font-family:'Lato',sans-serif;font-weight:700}
  .brand-mark{width:54px;height:54px;border-radius:50%;background:var(--ink-strong);margin:0 auto 8px}
  .brand-name{font-size:17px;line-height:1.15}
  .brand-tagline{font-size:12px;line-height:1.3;margin-top:2px}
  .contact{position:absolute;left:540px;top:95px;font-family:'Montserrat',sans-serif;font-size:13px;color:var(--ink)}
  .contact-rule{width:25px;height:3px;background:var(--green);margin-bottom:12px}
  .contact-item{display:flex;align-items:center;height:16.5px}
  .contact-item svg{width:11px;height:11px;margin-right:8px;fill:var(--green)}
  .letter{position:absolute;left:85px;width:623px;font-size:12.5px;line-height:18.7px}
  .date{top:246px}
  .recipient{top:283px}
  .recipient strong{font-weight:700;color:var(--ink-strong)}
  .salutation{top:376px}
  .body{top:414px}
  .body p{text-align:justify;margin-bottom:18.7px}
  .closing{top:824px}
  .signature{position:absolute;left:85px;top:846px;font-family:'Pinyon Script',cursive;font-size:26px;color:var(--ink-strong)}
  .footer-band{position:absolute;left:0;top:1070px;width:793px;height:38px;background:var(--band)}
  .footer-accent{position:absolute;left:720px;top:1070px;width:73px;height:38px;background:var(--green)}
  .footer-text{position:absolute;left:57px;top:1070px;height:38px;display:flex;align-items:center;font-family:'Montserrat',sans-serif;font-size:13px;color:var(--white)}
  .footer-text strong{font-weight:600;margin-right:5px}
  .footer-mark{position:absolute;left:676px;top:1064px;width:50px;height:50px;border-radius:50%;background:var(--ink-strong);border:3px solid var(--white)}
</style>
</head>
<body>
<main class="letterhead">
  <header class="brand">
    <div class="brand-mark"></div>
    <div class="brand-name">Korbin Ventilation's</div>
    <div class="brand-tagline">"We're Dalton beyond the pack"</div>
  </header>

  <address class="contact" style="font-style:normal">
    <div class="contact-rule"></div>
    <div class="contact-item"><svg viewBox="0 0 24 24"><path d="M6.6 10.8a15.1 15.1 0 0 0 6.6 6.6l2.2-2.2c.3-.3.7-.4 1-.2 1.1.4 2.3.6 3.6.6.6 0 1 .4 1 1V20c0 .6-.4 1-1 1A17 17 0 0 1 3 4c0-.6.4-1 1-1h3.5c.6 0 1 .4 1 1 0 1.3.2 2.5.6 3.6.1.3 0 .7-.2 1z"/></svg>210.555.0190</div>
    <div class="contact-item"><svg viewBox="0 0 24 24"><path d="M2 5h20v14H2z M2 5l10 8 10-8" fill="none" stroke="#a3b243" stroke-width="2.5"/></svg>info@korbinventilation.com</div>
    <div class="contact-item"><svg viewBox="0 0 24 24"><circle cx="12" cy="12" r="9.5" fill="none" stroke="#a3b243" stroke-width="2"/><path d="M2.5 12h19M12 2.5c3 3 3 16 0 19M12 2.5c-3 3-3 16 0 19" fill="none" stroke="#a3b243" stroke-width="1.6"/></svg>www.korbinventilation.com</div>
  </address>

  <p class="letter date">01 January 2050</p>
  <p class="letter recipient"><strong>Company (Pvt) Ltd.</strong><br>PO Box 4417 Brookfield St<br>Sample City Country 3355</p>
  <p class="letter salutation">Dear Nora Ellwood,</p>

  <section class="letter body">
    <p>Lorem ipsum dolor sit amet, consectetuer adipiscing elit, sed diam nonummy nibh euismod tincidunt ut laoreet dolore magna aliquam erat volutpat. Ut wisi enim ad minim veniam, quis nostrud exerci tation ullamcorper suscipit lobortis nisl ut aliquip ex ea commodo consequat. Duis dolore te feugait nulla facilisi. Nam liber tempor cum soluta nobis eleifend option congue nihil imperdiet doming id quod mazim placerat facer possim assum. Lorem ipsum dolor sit amet, consectetuer adipiscing elit, sed diam nonummy nibh euismod tincidunt ut laoreet dolore magna aliquam erat volutpat. Ut wisi enim ad minim veniam, quis nostrud exerci tation ullamcorper suscipit lobortis nisl ut aliquip ex ea commodo consequat.</p>
    <p>Consectetuer adipiscing elit, sed diam nonummy nibh euismod tincidunt ut laoreet dolore magna aliquam erat volutpat. Ut wisi enim ad minim veniam, quis nostrud exerci tation ullamcorper suscipit lobortis nisl ut aliquip ex ea commodo consequat. Consectetuer adipiscing elit, sed diam nonummy nibh euismod tincidunt ut laoreet dolore magna aliquam erat volutpat. Ut wisi enim ad minim veniam, quis nostrud exerci tation ullamcorper suscipit lobortis nisl ut aliquip ex ea commodo consequat.</p>
    <p>Consectetuer adipiscing elit, sed diam nonummy nibh euismod tincidunt ut laoreet dolore magna aliquam erat volutpat. Ut wisi enim ad minim veniam, quis nostrud exerci tation ullamcorper suscipit lobortis nisl ut aliquip ex ea commodo consequat. Consectetuer adipiscing elit, sed diam nonummy nibh euismod tincidunt ut laoreet dolore magna aliquam erat volutpat. Ut wisi enim ad minim veniam, quis nostrud exerci tation ullamcorper suscipit lobortis nisl ut aliquip ex ea commodo consequat.</p>
  </section>

  <p class="letter closing">Sincerely Yours</p>
  <p class="signature">Julian Marsh Corwin</p>

  <footer>
    <div class="footer-band"></div>
    <div class="footer-accent"></div>
    <div class="footer-text"><strong>Korbin Ventilation GmbH &amp; Co,</strong> City/State, Alder Road, PO Box, Zip 4000, Australia</div>
    <div class="footer-mark"></div>
  </footer>
</main>
</body>
</html>
```